Valdorra Holdings Real Estate Company business cards

New business card design, we are generally happy with the basic layout of the existing front of business card, (feel free to change) but require a head shot photo on the back side.

http://www.valdorra.com.au/

Attached logos, and existing business card

------------------------------

Target Market(s)

Real estate

Industry/Entity Type

Real Estate

Contact Information for Business Card

Standard size double sided

Font styles to use
Other font styles liked:
• Futura

Requirements
Must have
• Photo head shot on the back side
Nice to have
• yes
Should not have
• No

```html
<!DOCTYPE html>
<html lang="en">
<head>
<meta charset="utf-8">
<title>Valdorra Holdings – Business Cards</title>
<link href="https://fonts.googleapis.com/css2?family=Jost:wght@400;500&family=Roboto:wght@400;500&display=swap" rel="stylesheet">
<style>
  :root {
    --bg: #e6e6e8;
    --purple-dark: #2a1450;
    --purple: #3d1f6e;
    --purple-light: #4b2a82;
    --orange: #f28a1a;
    --white: #ffffff;
    --muted: #d8cfe8;
  }
  * { box-sizing: border-box; margin: 0; padding: 0; }
  html, body { width: 1200px; height: 1200px; overflow: hidden; }
  body {
    background: var(--bg);
    font-family: "Jost", "Futura", sans-serif;
    position: relative;
  }
  .card {
    position: absolute;
    left: 180px;
    width: 840px;
    height: 480px;
    border-radius: 30px;
    overflow: hidden;
    background: linear-gradient(160deg, var(--purple-light) 0%, var(--purple) 45%, var(--purple-dark) 100%);
    color: var(--white);
    box-shadow: 0 10px 24px rgba(0,0,0,0.18);
  }
  .card-front { top: 90px; }
  .card-back { top: 630px; }

  /* Front */
  .headshot {
    position: absolute;
    top: 0; right: 0;
    width: 410px; height: 400px;
    background: linear-gradient(180deg, #f2f2f4 0%, #e9e6e6 45%, #8d8fa5 75%, #2a3352 100%);
  }
  .tagline {
    position: absolute;
    left: 60px; top: 160px;
    font-size: 44px;
    font-weight: 400;
    line-height: 1.08;
  }
  .tagline .accent { color: var(--orange); }
  .brand {
    font-family: "Jost", "Futura", sans-serif;
    font-weight: 400;
    color: var(--white);
    white-space: nowrap;
  }
  .card-front .brand {
    position: absolute;
    left: 60px; top: 350px;
    font-size: 50px;
  }

  /* Back */
  .card-back .brand {
    position: absolute;
    left: 60px; top: 120px;
    font-size: 66px;
  }
  .rule {
    position: absolute;
    height: 1.5px;
    background: var(--muted);
    opacity: 0.8;
  }
  .rule-brand { left: 60px; top: 290px; width: 500px; }
  .rule-person { left: 560px; top: 98px; width: 240px; }
  .person {
    position: absolute;
    right: 40px; top: 36px;
    text-align: right;
  }
  .person-name {
    font-family: "Roboto", sans-serif;
    font-weight: 500;
    font-size: 30px;
    color: var(--orange);
  }
  .person-role {
    position: absolute;
    right: 40px; top: 106px;
    font-family: "Roboto", sans-serif;
    font-size: 17px;
  }
  .find-us {
    position: absolute;
    right: 40px; top: 150px;
    display: flex; align-items: center; gap: 6px;
    font-family: "Roboto", sans-serif;
    font-size: 20px;
  }
  .find-us .label { margin-right: 6px; }
  .social-square {
    width: 24px; height: 24px;
    border-radius: 4px;
    background: var(--orange);
  }
  .abn {
    position: absolute;
    right: 40px; top: 196px;
    font-family: "Roboto", sans-serif;
    font-size: 20px;
  }
  .abn .label { color: var(--orange); }
  .contact-list {
    position: absolute;
    left: 60px; top: 318px;
    list-style: none;
    font-family: "Roboto", sans-serif;
    font-size: 21px;
  }
  .contact-list li {
    display: flex; align-items: center; gap: 16px;
    height: 38px;
  }
  .contact-list svg { width: 22px; height: 22px; flex: none; }
  .accent-band {
    position: absolute;
    right: 0; bottom: 0;
    width: 330px; height: 150px;
    background: var(--orange);
    clip-path: polygon(0 100%, 0 60%, 100% 0, 100% 100%);
  }
</style>
</head>
<body>
  <section class="card card-front">
    <div class="headshot" role="img" aria-label="Head shot of the director in a dark suit and blue tie on a light background"></div>
    <p class="tagline">Let us<br>show you<br><span class="accent">property</span></p>
    <p class="brand">Valdorra Holdings</p>
  </section>

  <section class="card card-back">
    <p class="brand">Valdorra Holdings</p>
    <div class="rule rule-brand"></div>

    <div class="person"><p class="person-name">Marcus Lim</p></div>
    <div class="rule rule-person"></div>
    <p class="person-role">Director</p>

    <div class="find-us">
      <span class="label">Find us:</span>
      <span class="social-square"></span>
      <span class="social-square"></span>
      <span class="social-square"></span>
    </div>
    <p class="abn"><span class="label">ABN:</span> 47 215 903 618</p>

    <ul class="contact-list">
      <li>
        <svg viewBox="0 0 24 24" aria-hidden="true"><rect x="6" y="2" width="12" height="20" rx="2" fill="#f28a1a"/><rect x="8" y="5" width="8" height="12" fill="#3d1f6e"/><circle cx="12" cy="19.5" r="1" fill="#3d1f6e"/></svg>
        0412 555 309
      </li>
      <li>
        <svg viewBox="0 0 24 24" aria-hidden="true"><circle cx="12" cy="12" r="9" fill="none" stroke="#f28a1a" stroke-width="2"/><ellipse cx="12" cy="12" rx="4" ry="9" fill="none" stroke="#f28a1a" stroke-width="2"/><line x1="3" y1="12" x2="21" y2="12" stroke="#f28a1a" stroke-width="2"/></svg>
        www.valdorra.com.au
      </li>
      <li>
        <svg viewBox="0 0 24 24" aria-hidden="true"><rect x="2" y="5" width="20" height="14" rx="1" fill="#f28a1a"/><polyline points="2,6 12,13 22,6" fill="none" stroke="#3d1f6e" stroke-width="2"/></svg>
        marcus.lim@valdorra.com.au
      </li>
    </ul>

    <div class="accent-band"></div>
  </section>
</body>
</html>
```